Healthy Snack Bar Wrapper Design

We are passionate about delivering healthy and tasty treats that are Raw, Organic, Preservative Free, Gluten Free, have No Added Sugar and No Additives!
In this project we are looking for a design for a new healthy food product to be launched soon in Australia. The packaging will be a bar wrapper made from foil that will be hot sealed, with a front and a back.
The snack is a raw, organic and healthy treat made predominantly with nuts, and will come in 3 initial flavours:
- Black Forest (Sour Cherry and Choc)
- Plum Parade (Banana, Apricot and Blueberry)
- Zestivalle (Pineapple, Passionfruit and Kiwi)
The product name is Pebblyx, which does not currently have a logo. We are happy to have this as a simple written component of the initial design at the top of the packaging, perhaps within an circle, square or oval.
The typeface used for the names and the main ingredients should be fun.
The overall design should be very simple and make use of minimal colours. Our preferences are to have a plain colour for the background, such as light organic brown or white, with an eye catching colour that can be used to define the flavour, but should not be too vibrant.
We do not want to have an 3 dimensional images or objects. Nor do we want to have product images and any imagery should be only to give the impression of the flavours within rather than an image of the flavour. Finally, we do not want to have gradients included in the design.
The final design should communicate healthy, tasty and fun!
Examples of inspiration designs are attached in the files.
Main Information:
- The front should comprise of the following information:
-- Pebblyx
-- Flavour name (such as Black Forest)
-- Main Ingredients (Sour Cherry and Choc) (This is optional)
-- Portion size (60g)
-- Message (This is optional)
--- 0% Additives
--- 60% Nuts
--- 100% Natural
- The back needs to have space for the following information:
-- Nutritional Information
-- Barcode
-- Ingredients
-- Contact information
- Wrapper Dimensions
-- Width: 14cm
-- Height: 15cm
- Bar Dimensions
-- Width: 3cm
-- Height: 10cm
-- Depth: 2.5cm
Target Market(s)
People who want to have a healthy tasty treat
Colors
Designer to choose colors to be used in the design.
Requirements
Must have
- Main Information:
- - The front should comprise of the following information:
- -- Pebblyx
- -- Flavour name (such as Black Forest)
- -- Main Ingredients (Sour Cherry and Choc) (This is optional)
- -- Portion size (60g)
- -- Message (This is optional)
- --- 0% Additives
- --- 60% Nuts
- --- 100% Natural
- - The back needs to have space for the following information:
- -- Nutritional Information
- -- Barcode
- -- Ingredients
- -- Contact information
- - Wrapper Dimensions
- -- Width: 14cm
- -- Height: 15cm
- - Bar Dimensions
- -- Width: 3cm
- -- Height: 10cm
- -- Depth: 2.5cm
Should not have
- We do not want to have an 3 dimensional images or objects. Nor do we want to have product images and any imagery should be only to give the impression of the flavours within rather than an image of the flavour. Finally, we do not want to have gradients included in the design.

```html
<!DOCTYPE html>
<html lang="en">
<head>
<meta charset="utf-8">
<title>Pebblyx – Snack Bar Wrappers</title>
<link href="https://fonts.googleapis.com/css2?family=Fredoka:wght@500;600&family=Amatic+SC:wght@700&family=Didact+Gothic&display=swap" rel="stylesheet">
<style>
  :root {
    --canvas: #e4e4e4;
    --foil-white: #ffffff;
    --ink: #333333;
    --badge: #3a3a3a;
    --plum: #c766a6;
    --cherry: #eaa238;
    --zest: #b9c825;
  }
  * { box-sizing: border-box; margin: 0; padding: 0; }
  html, body { width: 1200px; height: 1200px; overflow: hidden; }
  body {
    background: var(--canvas);
    font-family: "Didact Gothic", sans-serif;
    color: var(--ink);
  }
  .svg-defs { position: absolute; width: 0; height: 0; }
  .range {
    display: flex;
    justify-content: center;
    gap: 60px;
    padding-top: 250px;
  }
  .wrapper {
    width: 300px;
    color: var(--flavour);
  }
  .wrapper--plum { --flavour: var(--plum); }
  .wrapper--cherry { --flavour: var(--cherry); }
  .wrapper--zest { --flavour: var(--zest); }

  .seal-edge { display: block; width: 300px; height: 12px; }
  .seal-edge--top { color: var(--flavour); }
  .seal-edge--bottom { color: var(--foil-white); }

  .wrapper__cap {
    background: var(--flavour);
    height: 200px;
    display: flex;
    align-items: flex-end;
    justify-content: center;
    padding-bottom: 26px;
  }
  .brand-badge {
    width: 118px;
    height: 118px;
    border-radius: 50%;
    background: var(--badge);
    display: flex;
    align-items: center;
    justify-content: center;
  }
  .brand-badge__name {
    font-family: "Fredoka", sans-serif;
    font-weight: 500;
    font-size: 23px;
    color: #ffffff;
    letter-spacing: 0.5px;
  }

  .wrapper__body {
    background: var(--foil-white);
    padding: 30px 34px 0;
    height: 420px;
    text-align: center;
  }
  .flavour-name {
    font-family: "Fredoka", sans-serif;
    font-weight: 600;
    font-size: 44px;
    line-height: 0.98;
    color: var(--ink);
    text-transform: uppercase;
    letter-spacing: -0.5px;
  }
  .flavour-notes {
    font-family: "Amatic SC", sans-serif;
    font-weight: 700;
    font-size: 34px;
    line-height: 1;
    color: var(--flavour);
    margin-top: 14px;
    min-height: 68px;
  }
  .claims {
    list-style: none;
    margin-top: 18px;
    border-top: 2px solid var(--flavour);
  }
  .claims__item {
    border-bottom: 2px solid var(--flavour);
    padding: 6px 0 5px;
    font-size: 17px;
    color: var(--ink);
    text-align: left;
    padding-left: 56px;
  }
  .claims__figure { font-family: "Fredoka", sans-serif; font-weight: 600; font-size: 20px; }
  .portion {
    font-family: "Fredoka", sans-serif;
    font-weight: 600;
    font-size: 32px;
    color: var(--ink);
    margin-top: 26px;
  }
</style>
</head>
<body>
<svg class="svg-defs" aria-hidden="true">
  <defs>
    <pattern id="teeth-up" width="10" height="12" patternUnits="userSpaceOnUse">
      <path d="M0 12 L5 0 L10 12 Z" fill="#fff"/>
    </pattern>
    <pattern id="teeth-down" width="10" height="12" patternUnits="userSpaceOnUse">
      <path d="M0 0 L5 12 L10 0 Z" fill="#fff"/>
    </pattern>
    <mask id="mask-teeth-up"><rect width="300" height="12" fill="url(#teeth-up)"/></mask>
    <mask id="mask-teeth-down"><rect width="300" height="12" fill="url(#teeth-down)"/></mask>
  </defs>
</svg>

<main class="range">
  <article class="wrapper wrapper--plum">
    <svg class="seal-edge seal-edge--top" viewBox="0 0 300 12"><rect width="300" height="12" fill="currentColor" mask="url(#mask-teeth-up)"/></svg>
    <div class="wrapper__cap">
      <div class="brand-badge"><span class="brand-badge__name">Pebblyx</span></div>
    </div>
    <div class="wrapper__body">
      <h2 class="flavour-name">Plum<br>Parade</h2>
      <p class="flavour-notes">Banana, Apricot<br>&amp; Blueberry</p>
      <ul class="claims">
        <li class="claims__item"><span class="claims__figure">0%</span> additives</li>
        <li class="claims__item"><span class="claims__figure">60%</span> nuts</li>
        <li class="claims__item"><span class="claims__figure">100%</span> natural</li>
      </ul>
      <p class="portion">60g</p>
    </div>
    <svg class="seal-edge seal-edge--bottom" viewBox="0 0 300 12"><rect width="300" height="12" fill="currentColor" mask="url(#mask-teeth-down)"/></svg>
  </article>

  <article class="wrapper wrapper--cherry">
    <svg class="seal-edge seal-edge--top" viewBox="0 0 300 12"><rect width="300" height="12" fill="currentColor" mask="url(#mask-teeth-up)"/></svg>
    <div class="wrapper__cap">
      <div class="brand-badge"><span class="brand-badge__name">Pebblyx</span></div>
    </div>
    <div class="wrapper__body">
      <h2 class="flavour-name">Black<br>Forest</h2>
      <p class="flavour-notes">Sour Cherry<br>&amp; Choc</p>
      <ul class="claims">
        <li class="claims__item"><span class="claims__figure">0%</span> additives</li>
        <li class="claims__item"><span class="claims__figure">60%</span> nuts</li>
        <li class="claims__item"><span class="claims__figure">100%</span> natural</li>
      </ul>
      <p class="portion">60g</p>
    </div>
    <svg class="seal-edge seal-edge--bottom" viewBox="0 0 300 12"><rect width="300" height="12" fill="currentColor" mask="url(#mask-teeth-down)"/></svg>
  </article>

  <article class="wrapper wrapper--zest">
    <svg class="seal-edge seal-edge--top" viewBox="0 0 300 12"><rect width="300" height="12" fill="currentColor" mask="url(#mask-teeth-up)"/></svg>
    <div class="wrapper__cap">
      <div class="brand-badge"><span class="brand-badge__name">Pebblyx</span></div>
    </div>
    <div class="wrapper__body">
      <h2 class="flavour-name">Zesti<br>valle</h2>
      <p class="flavour-notes">Pineapple, Kiwi<br>&amp; Passionfruit</p>
      <ul class="claims">
        <li class="claims__item"><span class="claims__figure">0%</span> additives</li>
        <li class="claims__item"><span class="claims__figure">60%</span> nuts</li>
        <li class="claims__item"><span class="claims__figure">100%</span> natural</li>
      </ul>
      <p class="portion">60g</p>
    </div>
    <svg class="seal-edge seal-edge--bottom" viewBox="0 0 300 12"><rect width="300" height="12" fill="currentColor" mask="url(#mask-teeth-down)"/></svg>
  </article>
</main>
</body>
</html>
```